Business card and Stationery for data intelligence company

We need a new design for our business cards and stationery (Business Letter templates and a Quote example on Word, but it MUST work on Google Doc as well).

We are a software company based in Ireland and UK. Our product is "Orvenza", data intelligence platform with beautiful visualizations, graph capabilities (things are interconnected), powerful, flexible, it can manage Big Data and Streaming information. It's modern and relatively open source.
Our company will provide data intelligence for law enforcements, pharmaceuticals, and similar high end customers.

We'll launch a new website soon. At the moment it's http://www.kovar-analytics.example if you want to take a look. This is our youtube channel in case you need it to understand what Orvenza is: https://www.youtube.com/c/kovaranalyticschannel

We changed the logo so please use the logo I attach here.

We'd like the output to be cool and modern but elegant and "business" at the same time. It should inspire simple sophistication, "unity" "intent" "purpose" yet subtly very advanced and innovative.

The name "Orvenza" does NOT refer to sirens (mithological creatures) as well as the warning devices. It means Kinetic Object Vector Analysis Reactor. Please use our logo's colors and if you want to something like the "graph" image.

```html
<!DOCTYPE html>
<html lang="en">
<head>
<meta charset="UTF-8">
<title>Orvenza Business Card</title>
<link href="https://fonts.googleapis.com/css2?family=Montserrat:wght@400;500;600&family=Open+Sans:wght@400;600&display=swap" rel="stylesheet">
<style>
  :root {
    --backdrop: #e6e6e4;
    --card-dark: #1d1d1f;
    --card-light: #f1f1ef;
    --gold: #f5a623;
    --ink: #3a3a3c;
    --shadow: 0 18px 40px rgba(0,0,0,0.18), 0 4px 10px rgba(0,0,0,0.12);
  }
  * { margin: 0; padding: 0; box-sizing: border-box; }
  html, body { width: 1200px; height: 900px; overflow: hidden; }
  body {
    background: var(--backdrop);
    position: relative;
    font-family: "Open Sans", Arial, sans-serif;
  }
  .card {
    position: absolute;
    width: 580px;
    height: 340px;
    border-radius: 22px;
    box-shadow: var(--shadow);
    overflow: hidden;
  }
  .card--front { left: 90px; top: 90px; background: var(--card-dark); }
  .card--back { left: 530px; top: 470px; background: var(--card-light); }

  .wordmark {
    position: absolute;
    display: flex;
    align-items: center;
    gap: 16px;
    font-family: "Montserrat", Arial, sans-serif;
    font-weight: 500;
    color: var(--gold);
    letter-spacing: 0.12em;
    line-height: 1;
    white-space: nowrap;
  }
  .wordmark__dot {
    width: 16px; height: 16px;
    border-radius: 50%;
    background: var(--gold);
    flex: none;
  }
  .card--front .wordmark { left: 0; right: 0; top: 112px; justify-content: center; font-size: 54px; }
  .front-rule {
    position: absolute;
    left: 0; right: 0; top: 250px;
    height: 4px;
    background: var(--gold);
  }

  .holder {
    position: absolute; left: 40px; top: 44px;
    padding-left: 16px;
    border-left: 6px solid var(--gold);
  }
  .holder__name {
    font-family: "Montserrat", Arial, sans-serif;
    font-size: 24px; line-height: 28px; font-weight: 400; color: var(--ink);
  }
  .holder__name strong { font-weight: 600; }
  .holder__title {
    font-family: "Montserrat", Arial, sans-serif;
    font-size: 15px; line-height: 20px; color: var(--gold);
  }

  .card--back .wordmark { right: 40px; top: 136px; font-size: 36px; gap: 12px; }
  .card--back .wordmark__dot { width: 12px; height: 12px; }

  .contact { position: absolute; left: 62px; bottom: 38px; list-style: none; }
  .contact__item {
    display: flex; align-items: flex-start; gap: 12px;
    font-size: 14px; line-height: 19px; color: var(--ink);
    margin-top: 7px;
  }
  .contact__icon { width: 14px; height: 14px; flex: none; margin-top: 3px; }
  .contact__icon svg { width: 14px; height: 14px; display: block; }
</style>
</head>
<body>

  <section class="card card--front" aria-label="Card front">
    <div class="wordmark"><span class="wordmark__dot"></span><span>ORVENZA</span></div>
    <div class="front-rule"></div>
  </section>

  <section class="card card--back" aria-label="Card back">
    <div class="holder">
      <p class="holder__name">Jonathan <strong>Doe</strong></p>
      <p class="holder__title">Job Title</p>
    </div>

    <div class="wordmark"><span class="wordmark__dot"></span><span>ORVENZA</span></div>

    <ul class="contact">
      <li class="contact__item">
        <span class="contact__icon"><svg viewBox="0 0 14 14"><path d="M7 1a4 4 0 0 0-4 4c0 3 4 8 4 8s4-5 4-8a4 4 0 0 0-4-4z" fill="var(--gold)"/><circle cx="7" cy="5" r="1.5" fill="#fff"/></svg></span>
        <span>Examplestreet Ave 63<br>12345 Sincity</span>
      </li>
      <li class="contact__item">
        <span class="contact__icon"><svg viewBox="0 0 14 14"><path d="M2 5c0-2 2-3 5-3s5 1 5 3v1H9V5H5v1H2z" fill="var(--gold)"/><rect x="3" y="7" width="8" height="5" rx="1" fill="var(--gold)"/><circle cx="7" cy="9.5" r="1.2" fill="#fff"/></svg></span>
        <span>000 000 0000</span>
      </li>
      <li class="contact__item">
        <span class="contact__icon"><svg viewBox="0 0 14 14"><rect x="1" y="3" width="12" height="8" fill="var(--gold)"/><path d="M1 3l6 5 6-5" fill="none" stroke="#fff" stroke-width="1.2"/></svg></span>
        <span>youremail@xyz.com</span>
      </li>
      <li class="contact__item">
        <span class="contact__icon"><svg viewBox="0 0 14 14"><circle cx="7" cy="7" r="5.5" fill="none" stroke="var(--gold)" stroke-width="1.4"/><path d="M1.5 7h11M7 1.5c-3 3-3 8 0 11M7 1.5c3 3 3 8 0 11" fill="none" stroke="var(--gold)" stroke-width="1"/></svg></span>
        <span>www.yourwebsite.com</span>
      </li>
    </ul>
  </section>

</body>
</html>
```